Brinevale Yacht Management Full Page Ad Flyer

Yacht Management Package also includes the following periodic Monthly services:

Monthly full vessel systems checklist inspections
Diver For Hull Cleaning And Inspection Of Props, Shafts, and Zincs
Interior/Exterior Detailing and scheduled washdowns
Manage Haulout
Pump-out Services
On-call Captain and Crew Services
Updates

Need more time to provide more content to designers and the printing press template file.

Target Market(s)

Vessel owners, motor yachts, sailboats from 25 feet in length up to 125 feet in length. We do not do cruise ships or yachts larger than 125 feet. Someone who has their boat docked at their house or a local marina. We also offer mobile on-site services.

```html
<!DOCTYPE html>
<html lang="en">
<head>
<meta charset="utf-8">
<title>Brinevale Yacht Management – Flyer</title>
<link href="https://fonts.googleapis.com/css2?family=Jost:wght@300;400;600;700&family=Poppins:wght@400;500;600&display=swap" rel="stylesheet">
<style>
  :root{
    --stage:#c3c3c4;
    --navy-deep:#0a1836;
    --navy:#0a3566;
    --ocean:#0d5ea8;
    --gold:#f2c81f;
    --white:#ffffff;
    --ink:#1b1b1b;
  }
  *{margin:0;padding:0;box-sizing:border-box}
  html,body{width:1200px;height:2192px;overflow:hidden;background:var(--stage)}
  .stage{position:relative;width:1200px;height:2192px}
  .flyer{
    position:absolute;left:40px;top:371px;
    width:896px;height:1160px;
    transform:scale(1.25);transform-origin:0 0;
    overflow:hidden;background:var(--navy-deep);
    box-shadow:0 20px 40px rgba(0,0,0,.35);
    font-family:"Poppins",sans-serif;color:var(--white);
  }
  .flyer-art{position:absolute;inset:0;width:896px;height:1160px}
  .brand{position:absolute;left:72px;top:130px;text-align:center;width:385px}
  .brand-name{font-family:"Jost",sans-serif;font-weight:400;font-size:46px;letter-spacing:9px;line-height:1}
  .brand-tag{font-family:"Jost",sans-serif;font-weight:400;font-size:11px;letter-spacing:9px;margin-top:14px}
  .contact{position:absolute;left:523px;top:104px;width:373px}
  .contact-label{color:var(--gold);font-size:20px;font-weight:400;padding-bottom:4px;border-bottom:1px solid rgba(255,255,255,.45)}
  .contact-phone{display:flex;align-items:center;gap:16px;margin-top:10px;font-weight:600;font-size:23px}
  .contact-phone svg{width:24px;height:24px}
  .headline{position:absolute;left:393px;top:452px;font-family:"Jost",sans-serif;line-height:.92}
  .headline-main{display:block;font-weight:700;font-size:60px;text-shadow:0 2px 6px rgba(0,0,0,.4)}
  .headline-sub{display:block;color:var(--gold);font-weight:400;font-size:46px;letter-spacing:17px;margin-top:8px}
  .services-title{position:absolute;left:0;top:756px;width:550px;padding-left:198px;padding-bottom:6px;border-bottom:1px solid rgba(255,255,255,.6);font-family:"Jost",sans-serif;line-height:1}
  .services-title .lead{display:block;font-weight:600;font-size:34px}
  .services-title .sub{display:block;color:var(--gold);font-weight:300;font-size:36px}
  .service-list{position:absolute;list-style:none;font-size:19px;font-weight:500;line-height:27px}
  .service-list li{position:relative;padding-left:17px;margin-bottom:14px}
  .service-list li::before{content:"";position:absolute;left:0;top:10px;width:7px;height:7px;background:var(--gold)}
  .service-list.left{left:111px;top:852px;width:400px}
  .service-list.right{left:551px;top:852px;width:250px}
  .service-list.right li{margin-bottom:41px}
  .service-list.right li:last-child{margin-bottom:0}
  .footer{position:absolute;left:0;bottom:0;width:896px;height:83px;background:var(--white);color:var(--ink);font-family:"Jost",sans-serif;font-size:24px;font-weight:400;text-align:center;padding-top:10px}
</style>
</head>
<body>
<div class="stage">
  <article class="flyer">
    <svg class="flyer-art" viewBox="0 0 896 1160">
      <defs>
        <linearGradient id="sky" x1="0" y1="0" x2="1" y2="1">
          <stop offset="0" stop-color="#0a1836"/>
          <stop offset=".6" stop-color="#0a3566"/>
          <stop offset="1" stop-color="#0b4a85"/>
        </linearGradient>
        <linearGradient id="sunset" x1="0" y1="0" x2="0" y2="1">
          <stop offset="0" stop-color="#e8870f"/>
          <stop offset=".3" stop-color="#f2a01e"/>
          <stop offset=".6" stop-color="#9a4114"/>
          <stop offset="1" stop-color="#2e140c"/>
        </linearGradient>
        <linearGradient id="marina" x1="0" y1="0" x2="1" y2="1">
          <stop offset="0" stop-color="#d9d2bd"/>
          <stop offset=".5" stop-color="#a89c78"/>
          <stop offset="1" stop-color="#4a4838"/>
        </linearGradient>
        <linearGradient id="water" x1="0" y1="0" x2="0" y2="1">
          <stop offset="0" stop-color="#1c4760"/>
          <stop offset=".5" stop-color="#10283a"/>
          <stop offset="1" stop-color="#0b1524"/>
        </linearGradient>
        <linearGradient id="waveTone" x1="0" y1="0" x2="1" y2="0">
          <stop offset="0" stop-color="#1560a8"/>
          <stop offset=".6" stop-color="#3f6f9e"/>
          <stop offset="1" stop-color="#9aa6b4"/>
        </linearGradient>
        <linearGradient id="waveToneLow" x1="0" y1="0" x2="1" y2="0">
          <stop offset="0" stop-color="#5d7a98"/>
          <stop offset="1" stop-color="#a9b1ba"/>
        </linearGradient>
        <clipPath id="circleClip"><circle cx="20" cy="615" r="210"/></clipPath>
      </defs>
      <rect width="896" height="1160" fill="url(#sky)"/>
      <g role="img" aria-label="Photo: sailboat on the sea at sunset">
        <path d="M0 330 C 300 320 600 350 896 420 L896 760 C 700 750 450 700 300 620 C 220 575 120 560 0 570 Z" fill="url(#sunset)"/>
      </g>
      <g role="img" aria-label="Photo: deck of a yacht with coiled ropes at dusk">
        <path d="M0 570 C 120 560 220 575 300 620 C 450 700 700 750 896 760 L896 1077 L0 1077 Z" fill="url(#water)"/>
      </g>
      <path role="img" aria-label="Decorative blue and silver wave band" d="M0 230 C 300 225 600 270 896 345 L896 420 C 600 350 300 320 0 330 Z" fill="url(#waveTone)" opacity=".9"/>
      <path role="img" aria-label="Decorative silver wave band" d="M230 575 C 420 680 640 725 896 735 L896 790 C 640 790 420 730 230 575 Z" fill="url(#waveToneLow)" opacity=".85"/>
      <g role="img" aria-label="Photo: motor yacht moored at a marina beside city towers">
        <g clip-path="url(#circleClip)"><rect x="-200" y="400" width="440" height="430" fill="url(#marina)"/></g>
      </g>
      <circle cx="20" cy="615" r="214" fill="none" stroke="#dfe3e8" stroke-width="2"/>
    </svg>

    <div class="brand">
      <div class="brand-name">BRINEVALE</div>
      <div class="brand-tag">YACHT MANAGEMENT</div>
    </div>

    <div class="contact">
      <div class="contact-label">For More Details</div>
      <div class="contact-phone">
        <svg viewBox="0 0 24 24" aria-hidden="true"><path d="M6.6 3.5l2.3 3.4-1.6 1.8c.9 2.3 2.8 4.2 5 5.1l1.8-1.6 3.4 2.3-1.2 3.2c-.3.7-1 1-1.8.9C9 17.8 5.4 14.3 4.6 8.6c-.1-.8.2-1.5.9-1.8z" fill="#fff"/><path d="M15 4a6 6 0 0 1 5 5M15 7a3 3 0 0 1 2 2" stroke="#fff" stroke-width="1.6" fill="none"/></svg>
        <span>+0 000-000-0000</span>
      </div>
    </div>

    <h1 class="headline">
      <span class="headline-main">YACHT</span>
      <span class="headline-main">MANAGEMENT</span>
      <span class="headline-sub">PACKAGE</span>
    </h1>

    <h2 class="services-title"><span class="lead">PERIODIC</span><span class="sub">MONTHLY SERVICES:</span></h2>

    <ul class="service-list left">
      <li>Monthly full vessel systems<br>checklist inspections</li>
      <li>Diver For Hull Cleaning And Inspection<br>Of Props, Shafts, and Zincs</li>
      <li>Interior/Exterior Detailing and<br>scheduled washdowns</li>
    </ul>
    <ul class="service-list right">
      <li>Manage Haulout</li>
      <li>Pump-out Services</li>
      <li>On-call Captain and<br>Crew Services</li>
    </ul>

    <footer class="footer">www.brinevale-yachtmanagement.com</footer>
  </article>
</div>
</body>
</html>
```